Business Card Design Project

We are looking for a new business card design for a Drilling company in WA, Australia.

We are in between offices, however require a design in the meantime due to some upcoming events with our basic information.

The Logo for our company is Blue and Grey and would like this colour scheme throughout.

We are quite a new company so would like a memorable design that stands out and communicates a strong commitment to safety, quality of work and performance.

The company name is Ridgeback Boring Works (RBW)

The details to be included are as follows:

Martin Calloway
Managing Director
m.0481639027
e.martin@rbwgroup.com.au

Simon Calloway
Director
m.0429561384
e.simon@rbwgroup.com.au

Industry/Entity Type

Events

Requirements
Must have
• Under the Logo, we would like 'Western Australia'

```html
<!DOCTYPE html>
<html lang="en">
<head>
<meta charset="utf-8">
<title>Ridgeback Boring Works – Business Card</title>
<link rel="stylesheet" href="https://fonts.googleapis.com/css2?family=Oswald:wght@600&family=Arimo:wght@400&display=swap">
<style>
  :root {
    --backdrop: #dcdcdc;
    --card-black: #000000;
    --brand-navy: #123a7a;
    --panel-blue: #0b2f5e;
    --rule-grey: #a9a9a9;
    --contact-grey: #a3a8b0;
    --contact-white: #e9ecf2;
    --oval-white: #ffffff;
    --oval-shadow: #9b9b9b;
    --ghost-grey: #1c1c1c;
    --plate-white: #fbfbfc;
  }
  * { margin: 0; padding: 0; box-sizing: border-box; }
  html, body {
    width: 1200px; height: 900px; overflow: hidden;
    background: var(--backdrop);
  }
  .canvas { position: relative; width: 1200px; height: 900px; }

  .card {
    position: absolute; width: 571px; height: 379px;
    background: var(--card-black); overflow: hidden;
  }
  .card--front { left: 108px; top: 68px; }
  .card--back { left: 542px; top: 457px; }

  .front-oval { position: absolute; left: 0; top: 0; }

  .wordmark {
    position: absolute;
    font-family: "Oswald", "Arial Narrow", sans-serif;
    font-weight: 600; color: var(--brand-navy);
    text-transform: uppercase; line-height: 0.98;
  }
  .wordmark__square {
    display: inline-block; width: 16px; height: 16px;
    background: var(--brand-navy); margin-right: 10px; vertical-align: 6px;
  }
  .region {
    position: absolute;
    font-family: "Arimo", Arial, sans-serif;
    font-size: 11.5px; letter-spacing: 2.6px;
    color: var(--brand-navy); white-space: nowrap;
  }
  .card--front .wordmark { left: 30px; top: 44px; font-size: 29px; }
  .card--front .region { left: 72px; top: 135px; }

  .ghost-initials {
    position: absolute; right: 12px; top: 18px;
    font-family: "Oswald", "Arial Narrow", sans-serif;
    font-weight: 600; font-size: 92px; color: var(--ghost-grey);
    letter-spacing: 2px;
  }

  .rule {
    position: absolute; height: 2px; background: var(--rule-grey);
  }
  .card--front .rule { left: 35px; right: 34px; top: 215px; }
  .card--back .rule { left: 35px; right: 34px; top: 116px; }

  .contact-panel {
    position: absolute; left: 35px; right: 34px; top: 228px; height: 135px;
    background: var(--panel-blue);
    display: flex; justify-content: space-around; padding-top: 21px;
    font-family: "Arimo", Arial, sans-serif; text-align: center;
  }
  .contact__name, .contact__role {
    font-size: 17px; line-height: 20px; color: var(--contact-grey);
  }
  .contact__mobile, .contact__email {
    font-size: 15.5px; color: var(--contact-white); margin-top: 7px;
  }
  .contact__mobile { margin-top: 9px; }

  .logo-plate {
    position: absolute; left: 35px; right: 34px; top: 129px; height: 135px;
    background: var(--plate-white);
  }
  .card--back .wordmark { left: 118px; top: 14px; font-size: 27px; }
  .card--back .region { left: 170px; top: 104px; }
</style>
</head>
<body>
<main class="canvas">
  <section class="card card--front">
    <svg class="front-oval" width="571" height="379" viewBox="0 0 571 379" aria-hidden="true">
      <ellipse cx="170" cy="98" rx="222" ry="110" fill="var(--oval-shadow)"/>
      <ellipse cx="164" cy="88" rx="220" ry="106" fill="var(--oval-white)"/>
    </svg>
    <div class="ghost-initials" aria-hidden="true">RBW</div>
    <div class="wordmark"><span class="wordmark__square"></span>Ridgeback<br>Boring Works</div>
    <div class="region">Western Australia</div>
    <div class="rule"></div>
    <div class="contact-panel">
      <div class="contact">
        <p class="contact__name">Martin Calloway</p>
        <p class="contact__role">Managing Director</p>
        <p class="contact__mobile">m.0481639027</p>
        <p class="contact__email">e.martin@rbwgroup.com.au</p>
      </div>
      <div class="contact">
        <p class="contact__name">Simon Calloway</p>
        <p class="contact__role">Director</p>
        <p class="contact__mobile">m.0429561384</p>
        <p class="contact__email">e.simon@rbwgroup.com.au</p>
      </div>
    </div>
  </section>

  <section class="card card--back">
    <div class="rule"></div>
    <div class="logo-plate">
      <div class="wordmark"><span class="wordmark__square"></span>Ridgeback<br>Boring Works</div>
      <div class="region">Western Australia</div>
    </div>
  </section>
</main>
</body>
</html>
```